Marcus Penhale Logo and Wine Lable design

• What I am looking for is a packaging design to represent my product. The message I am looking for is a representation of western royal culture. Expensive and elegant. I want the label to look old, like from ancient times, feels like full of story, yet outstanding on the shelf among others. Special printing technique or paper can be used for an aged appearance.
• The packaging should include the logo, bottle, and the box that contains 12 bottle of wine.
• Shiraz
• Brand name Marcus Penhale must be included.
• Logo design should follow the same concept as above.
• There must be two labels, one on the front and one on the back of the bottle. The front label will carry most of the graphical impact.
• The back label should include some text for the wine, this could be anything, it is up to the design to present the story or testing of the wine in the test, which should also follow the concept above.
• The back label must have a standard space for barcode
• The label of packaging solution should also compline with the Cask Origin Scheme of Vintner Board.
• Final artwork ready for the printer should be provided in PDF format on CD, and include all fonts, images etc needed for printing
Updates

Project Deadline Extended
Reason: Hi guys, I am extending the deadline of this project as i am still seeking the design that could fulfill all my requirements, most important of all, as wine label, designs need to compliance with the Australia wine label requirement. in the extension, I will provide feed back to my designers proactively to find the right design that fits my requirement. Tam

Project Deadline Extended
Reason: waiting on the finalization on same designs

Industry/Entity Type

Printer

```html
<!DOCTYPE html>
<html lang="en">
<head>
<meta charset="utf-8">
<title>Marcus Penhale Shiraz – Front Label</title>
<link href="https://fonts.googleapis.com/css2?family=Pinyon+Script&family=Tenor+Sans&family=Cormorant+Garamond:wght@500&display=swap" rel="stylesheet">
<style>
  :root {
    --paper-centre: #f6f6f3;
    --paper-mid: #eeebe2;
    --paper-edge: #d6cbb0;
    --ink-brown: #5b4b43;
    --ink-grey: #4f4a46;
    --wine-red: #a3191d;
    --rule: #6a5a50;
    --scene-light: #ebe9e6;
    --scene-mid: #b9b2ad;
  }
  html, body {
    margin: 0;
    padding: 0;
    width: 815px;
    height: 1200px;
    overflow: hidden;
    background: var(--paper-edge);
  }
  .label {
    position: relative;
    width: 815px;
    height: 1200px;
    background: radial-gradient(ellipse 70% 62% at 50% 48%, var(--paper-centre) 0%, var(--paper-centre) 45%, var(--paper-mid) 75%, var(--paper-edge) 100%);
    box-shadow: inset 0 0 14px rgba(120, 100, 70, 0.35);
    overflow: hidden;
  }
  .crest {
    position: absolute;
    top: 88px;
    left: 140px;
    width: 535px;
    height: 44px;
    display: flex;
    align-items: center;
    gap: 16px;
  }
  .crest-rule {
    flex: 1;
    height: 2px;
    background: var(--rule);
  }
  .crest-name {
    font-family: "Tenor Sans", sans-serif;
    font-size: 15px;
    letter-spacing: 3px;
    text-transform: uppercase;
    color: var(--wine-red);
    white-space: nowrap;
  }
  .brand-name {
    position: absolute;
    top: 236px;
    left: 0;
    width: 815px;
    margin: 0;
    text-align: center;
    font-family: "Pinyon Script", cursive;
    font-weight: 400;
    font-size: 76px;
    line-height: 1;
    color: var(--ink-brown);
  }
  .estate-scene {
    position: absolute;
    top: 395px;
    left: 192px;
    width: 424px;
    height: 275px;
    background: radial-gradient(ellipse 55% 50% at 50% 50%, var(--scene-mid) 0%, var(--scene-light) 70%, rgba(246, 246, 243, 0) 100%);
    opacity: 0.8;
  }
  .variety {
    position: absolute;
    top: 750px;
    left: 0;
    width: 815px;
    margin: 0;
    text-align: center;
    font-family: "Tenor Sans", sans-serif;
    font-weight: 400;
    font-size: 80px;
    line-height: 1;
    letter-spacing: 34px;
    text-indent: 34px;
    color: var(--wine-red);
  }
  .region {
    position: absolute;
    top: 888px;
    left: 0;
    width: 815px;
    margin: 0;
    text-align: center;
    font-family: "Pinyon Script", cursive;
    font-size: 60px;
    line-height: 1;
    color: var(--ink-brown);
  }
  .vintage {
    position: absolute;
    top: 974px;
    left: 0;
    width: 815px;
    margin: 0;
    text-align: center;
    font-family: "Tenor Sans", sans-serif;
    font-size: 27px;
    letter-spacing: 7px;
    text-indent: 7px;
    color: var(--wine-red);
  }
  .alcohol {
    position: absolute;
    top: 1090px;
    left: 0;
    width: 815px;
    margin: 0;
    text-align: center;
    font-family: "Cormorant Garamond", serif;
    font-weight: 500;
    font-size: 24px;
    color: var(--ink-grey);
  }
</style>
</head>
<body>
  <main class="label">
    <div class="crest">
      <span class="crest-rule"></span>
      <span class="crest-name">Marcus Penhale</span>
      <span class="crest-rule"></span>
    </div>

    <h1 class="brand-name">Marcus Penhale</h1>

    <div class="estate-scene" role="img" aria-label="Engraved sketch of a château above rows of vines with a horse-drawn harvest cart in the foreground"></div>

    <h2 class="variety">SHIRAZ</h2>
    <p class="region">Swan Hill</p>
    <p class="vintage">2012</p>
    <p class="alcohol">ALC 13.5% VOL.</p>
  </main>
</body>
</html>
```